Nadia Poulter - Powerpoint slides

I am an educator and lecturer - I use powerpoint slides for my presentations. I would like to use my current logo and branding to create personalised powerpoint presentations.

I need a file with so I can select my personalized Powerpoint slides: I would like 3 colour variations of the following slides (design and layout is the same for all colours, with just the colour shades change)
1. Title Slide
2. Title & Content
3. Section Header
4. 2 content slide
5. Blank Slide

Note on colours: 3+ variations would be great - suggest background colours to be Turqoise
Dark/Grey Charcoal \
White
PLUS one free choice colour scheme from the designers.

Target Market(s)

Physiotherapists
Yoga Teachers
Students (yoga students and physiotherapy students)
Medical Professionals

Industry/Entity Type

Health And Wellness

Font styles to use
Serif
Sans Serif

Colors
33b8a4
876aae
0255a3

Requirements
Must have
• See the slide types in the brief description.
• Each slide should stay pretty much in the same colour, just different intensity of the shade.
• Please use the designs from my uploaded files.
• 3+ different colour variations for the regular content for slides
Nice to have
• Background patterns over part of the screen.
Should not have
• Not too many colour variations - I have chosen the ones I like as examples.

```html
<!DOCTYPE html>
<html lang="en">
<head>
<meta charset="utf-8">
<title>Nadia Poulter – Presentation Slide Set</title>
<link href="https://fonts.googleapis.com/css2?family=Poiret+One&family=Raleway:wght@400;600&display=swap" rel="stylesheet">
<style>
  :root {
    --teal: #1b7f79;
    --teal-motif: #3fb3a6;
    --purple: #876aae;
    --purple-motif: #a68fc6;
    --blue: #0f55a0;
    --blue-motif: #3d7cc4;
    --white: #ffffff;
    --ink-soft: #8b7ca8;
    --text-grey: #9a9a9a;
    --motif-faint: #eeeaf3;
    --display: "Poiret One", sans-serif;
    --body: "Raleway", sans-serif;
  }
  * { box-sizing: border-box; margin: 0; padding: 0; }
  html, body { width: 1200px; height: 2571px; overflow: hidden; background: var(--white); }
  .sheet { position: relative; width: 1200px; height: 2571px; }

  .slide {
    position: absolute; width: 552px; height: 312px; overflow: hidden;
    box-shadow: 0 3px 6px rgba(0,0,0,.25);
    color: var(--white); font-family: var(--display);
  }
  .col-left { left: 24px; }
  .col-right { left: 624px; }
  .col-center { left: 319px; }

  .slide--teal { background: var(--teal); --motif: var(--teal-motif); }
  .slide--purple { background: var(--purple); --motif: var(--purple-motif); }
  .slide--blue { background: var(--blue); --motif: var(--blue-motif); }
  .slide--white { background: var(--white); --motif: var(--motif-faint); color: var(--ink-soft); }

  .motif {
    position: absolute; width: 320px; height: 320px; border-radius: 50%;
    background: radial-gradient(circle, var(--motif) 0%, var(--motif) 30%, transparent 70%);
    opacity: .75;
  }
  .motif--top-left { left: -50px; top: -150px; }
  .motif--bottom-right { left: 250px; top: 120px; }
  .motif--right { left: 380px; top: -20px; }
  .motif--left { left: -170px; top: -10px; }
  .slide--white .motif { opacity: 1; }

  .brand {
    position: absolute; top: 24px; display: flex; align-items: center; gap: 6px;
    font-family: var(--display); font-size: 15px; white-space: nowrap;
  }
  .brand__dot { width: 14px; height: 14px; border: 1.5px solid currentColor; border-radius: 50%; }
  .brand--right { right: 18px; }
  .brand--left { left: 22px; }
  .slide--white .brand { color: var(--purple); }

  .title-block { position: absolute; left: 20px; right: 22px; }
  .title-block--low { top: 214px; }
  .title-block--mid { top: 176px; }
  .title-block--mid-low { top: 195px; }
  .title-block--end { text-align: right; }
  .title-block__title { font-size: 31px; line-height: 1.1; letter-spacing: .3px; }
  .title-block__subtitle { font-family: var(--body); font-size: 9.5px; margin-top: 8px; opacity: .85; }

  .page-heading { position: absolute; left: 18px; top: 12px; font-size: 24px; color: var(--ink-soft); }
  .page-heading::after {
    content: ""; position: absolute; left: 0; top: 40px; width: 28px; height: 3px; background: var(--purple);
  }
  .footer-bar {
    position: absolute; left: 0; right: 0; bottom: 0; height: 14px; background: var(--purple);
    font-family: var(--body); font-size: 6.5px; color: var(--white);
    display: flex; align-items: center; padding-left: 18px;
  }
  .footer-bar__page {
    position: absolute; right: 16px; top: -3px; width: 22px; height: 17px; background: var(--white);
    color: #555; font-size: 7px; display: flex; align-items: center; justify-content: center;
  }

  .photo-band {
    position: absolute; left: 0; right: 0; top: 70px; height: 134px;
    background: linear-gradient(180deg, #9b86c0 0%, #7d64a8 55%, #8a73b2 100%);
  }
  .key-point {
    position: absolute; top: 84px; width: 160px; text-align: center; font-family: var(--body);
  }
  .key-point__photo {
    width: 68px; height: 68px; margin: 0 auto; border-radius: 50%; border: 2px solid var(--white);
  }
  .key-point__photo--dawn { background: radial-gradient(circle at 50% 40%, #f2e3c8, #8f86a8 70%); }
  .key-point__photo--sunset { background: linear-gradient(180deg, #f0a54a 0%, #d87b4a 45%, #2e5f86 60%, #1d3a5a 100%); }
  .key-point__photo--lotus { background: radial-gradient(circle at 50% 55%, #e8778f, #c24c6a 45%, #f3c1c9 75%); }
  .key-point__heading { margin-top: 54px; font-size: 8px; color: var(--ink-soft); }
  .key-point__text { margin-top: 5px; font-size: 5.5px; line-height: 1.6; color: var(--text-grey); padding: 0 8px; }

  .feature-photo {
    position: absolute; left: 20px; top: 72px; width: 250px; height: 152px;
    background: radial-gradient(ellipse at 55% 40%, #fbe9c6 0%, #e9a85c 25%, #6b5b55 60%, #2b2a30 100%);
  }
  .bullet-group { position: absolute; left: 300px; width: 235px; font-family: var(--body); color: var(--text-grey); }
  .bullet-group__lead { font-size: 6px; font-weight: 600; color: #7a6c94; padding-left: 8px; position: relative; }
  .bullet-group__lead::before {
    content: ""; position: absolute; left: 0; top: 2px; width: 3px; height: 3px; background: var(--purple);
  }
  .bullet-group__list { list-style: none; margin-top: 3px; padding-left: 16px; font-size: 5.5px; line-height: 1.7; }
  .bullet-group__list li::before { content: "– "; color: var(--purple); }
</style>
</head>
<body>
<main class="sheet">

  <!-- Title slides: motif top-left -->
  <section class="slide slide--teal col-left" style="top:0">
    <div class="motif motif--top-left" role="img" aria-label="Decorative lotus pattern"></div>
    <div class="brand brand--right"><span class="brand__dot"></span>Nadia Poulter</div>
    <div class="title-block title-block--low"><h1 class="title-block__title">Your Title Goes Here</h1><p class="title-block__subtitle">Your Subtitle Goes Here</p></div>
  </section>
  <section class="slide slide--purple col-right" style="top:0">
    <div class="motif motif--top-left" role="img" aria-label="Decorative lotus pattern"></div>
    <div class="brand brand--right"><span class="brand__dot"></span>Nadia Poulter</div>
    <div class="title-block title-block--low"><h1 class="title-block__title">Your Title Goes Here</h1><p class="title-block__subtitle">Your Subtitle Goes Here</p></div>
  </section>
  <section class="slide slide--blue col-left" style="top:326px">
    <div class="motif motif--top-left" role="img" aria-label="Decorative lotus pattern"></div>
    <div class="brand brand--right"><span class="brand__dot"></span>Nadia Poulter</div>
    <div class="title-block title-block--low"><h1 class="title-block__title">Your Title Goes Here</h1><p class="title-block__subtitle">Your Subtitle Goes Here</p></div>
  </section>

  <!-- Motif bottom-right -->
  <section class="slide slide--teal col-right" style="top:326px">
    <div class="motif motif--bottom-right" role="img" aria-label="Decorative lotus pattern"></div>
    <div class="brand brand--left"><span class="brand__dot"></span>Nadia Poulter</div>
    <div class="title-block title-block--mid"><h1 class="title-block__title">Your Title Goes Here</h1><p class="title-block__subtitle">Your Subtitle Goes Here</p></div>
  </section>
  <section class="slide slide--purple col-left" style="top:646px">
    <div class="motif motif--bottom-right" role="img" aria-label="Decorative lotus pattern"></div>
    <div class="brand brand--left"><span class="brand__dot"></span>Nadia Poulter</div>
    <div class="title-block title-block--mid"><h1 class="title-block__title">Your Title Goes Here</h1><p class="title-block__subtitle">Your Subtitle Goes Here</p></div>
  </section>
  <section class="slide slide--blue col-right" style="top:646px">
    <div class="motif motif--bottom-right" role="img" aria-label="Decorative lotus pattern"></div>
    <div class="brand brand--left"><span class="brand__dot"></span>Nadia Poulter</div>
    <div class="title-block title-block--mid"><h1 class="title-block__title">Your Title Goes Here</h1><p class="title-block__subtitle">Your Subtitle Goes Here</p></div>
  </section>

  <!-- Motif right edge -->
  <section class="slide slide--teal col-left" style="top:969px">
    <div class="motif motif--right" role="img" aria-label="Decorative lotus pattern"></div>
    <div class="brand brand--left"><span class="brand__dot"></span>Nadia Poulter</div>
    <div class="title-block title-block--mid-low"><h1 class="title-block__title">Your Title Goes Here</h1><p class="title-block__subtitle">Your Subtitle Goes Here</p></div>
  </section>
  <section class="slide slide--purple col-right" style="top:969px">
    <div class="motif motif--right" role="img" aria-label="Decorative lotus pattern"></div>
    <div class="brand brand--left"><span class="brand__dot"></span>Nadia Poulter</div>
    <div class="title-block title-block--mid-low"><h1 class="title-block__title">Your Title Goes Here</h1><p class="title-block__subtitle">Your Subtitle Goes Here</p></div>
  </section>
  <section class="slide slide--blue col-left" style="top:1289px">
    <div class="motif motif--right" role="img" aria-label="Decorative lotus pattern"></div>
    <div class="brand brand--left"><span class="brand__dot"></span>Nadia Poulter</div>
    <div class="title-block title-block--mid-low"><h1 class="title-block__title">Your Title Goes Here</h1><p class="title-block__subtitle">Your Subtitle Goes Here</p></div>
  </section>

  <!-- Motif left edge, right-aligned title -->
  <section class="slide slide--teal col-right" style="top:1289px">
    <div class="motif motif--left" role="img" aria-label="Decorative lotus pattern"></div>
    <div class="brand brand--right"><span class="brand__dot"></span>Nadia Poulter</div>
    <div class="title-block title-block--mid-low title-block--end"><h1 class="title-block__title">Your Title Goes Here</h1><p class="title-block__subtitle">Your Subtitle Goes Here</p></div>
  </section>
  <section class="slide slide--purple col-left" style="top:1608px">
    <div class="motif motif--left" role="img" aria-label="Decorative lotus pattern"></div>
    <div class="brand brand--right"><span class="brand__dot"></span>Nadia Poulter</div>
    <div class="title-block title-block--mid-low title-block--end"><h1 class="title-block__title">Your Title Goes Here</h1><p class="title-block__subtitle">Your Subtitle Goes Here</p></div>
  </section>
  <section class="slide slide--blue col-right" style="top:1608px">
    <div class="motif motif--left" role="img" aria-label="Decorative lotus pattern"></div>
    <div class="brand brand--right"><span class="brand__dot"></span>Nadia Poulter</div>
    <div class="title-block title-block--mid-low title-block--end"><h1 class="title-block__title">Your Title Goes Here</h1><p class="title-block__subtitle">Your Subtitle Goes Here</p></div>
  </section>

  <!-- Blank slide -->
  <section class="slide slide--white col-left" style="top:1930px">
    <div class="motif motif--bottom-right" role="img" aria-label="Faint decorative lotus pattern"></div>
    <h2 class="page-heading">Your Blank Slide</h2>
    <div class="brand brand--right"><span class="brand__dot"></span>Nadia Poulter</div>
    <footer class="footer-bar">Yoga Teachers Physiotherapists<span class="footer-bar__page">13</span></footer>
  </section>

  <!-- Three key point slide -->
  <section class="slide slide--white col-right" style="top:1930px">
    <h2 class="page-heading">Three Key Point Page</h2>
    <div class="brand brand--right"><span class="brand__dot"></span>Nadia Poulter</div>
    <div class="photo-band" role="img" aria-label="Photo of a person meditating by a lake, tinted purple"></div>
    <article class="key-point" style="left:26px">
      <div class="key-point__photo key-point__photo--dawn" role="img" aria-label="Photo of meditation at dawn"></div>
      <h3 class="key-point__heading">Heading Here</h3>
      <p class="key-point__text">A brief note on this point for your class and clients.</p>
    </article>
    <article class="key-point" style="left:196px">
      <div class="key-point__photo key-point__photo--sunset" role="img" aria-label="Photo of meditation at sunset"></div>
      <h3 class="key-point__heading">Heading Here</h3>
      <p class="key-point__text">A brief note on this point for your class and clients.</p>
    </article>
    <article class="key-point" style="left:366px">
      <div class="key-point__photo key-point__photo--lotus" role="img" aria-label="Photo of a pink lotus pose"></div>
      <h3 class="key-point__heading">Heading Here</h3>
      <p class="key-point__text">A brief note on this point for your class and clients.</p>
    </article>
    <footer class="footer-bar">Yoga Teachers Physiotherapists<span class="footer-bar__page">14</span></footer>
  </section>

  <!-- Image left slide -->
  <section class="slide slide--white col-center" style="top:2251px">
    <h2 class="page-heading">Image Left</h2>
    <div class="brand brand--right"><span class="brand__dot"></span>Nadia Poulter</div>
    <div class="feature-photo" role="img" aria-label="Photo of a person meditating by a lake at sunrise"></div>
    <div class="bullet-group" style="top:76px">
      <p class="bullet-group__lead">Key idea for this part of the session</p>
      <ul class="bullet-group__list"><li>Supporting detail goes here</li><li>Supporting detail goes here</li><li>Supporting detail goes here</li></ul>
    </div>
    <div class="bullet-group" style="top:136px">
      <p class="bullet-group__lead">Key idea for this part of the session</p>
      <ul class="bullet-group__list"><li>Supporting detail goes here</li><li>Supporting detail goes here</li><li>Supporting detail goes here</li></ul>
    </div>
    <div class="bullet-group" style="top:200px">
      <p class="bullet-group__lead">Key idea for this part of the session</p>
      <ul class="bullet-group__list"><li>Supporting detail goes here</li><li>Supporting detail goes here</li><li>Supporting detail goes here</li></ul>
    </div>
    <footer class="footer-bar">Yoga Teachers Physiotherapists<span class="footer-bar__page">15</span></footer>
  </section>

</main>
</body>
</html>
```